A new PowerPoint Template for a French consulting company

Who are we?

Formed in 2005, Quorv is a consulting company specialising in the human aspect of change and transformation.

From our offices in the heart of Paris, our team of 30 consultants work with leading organisations in the Aerospace, Finance, Transportation and Public sectors to deliver lasting change.

Our customers trust us with some of their most strategic and sensitive projects. They trust us with these projects because:
- We listen to them, ensuring we understand the real needs of their business
- We involve them, co-developing and tailoring our solutions to the specific challenges they face
- We’re professional, without taking ourselves too seriously
- We’re imaginative, whilst always remaining pragmatic
- We get results!

You can find out more about who we are and the work we do here: http://www.quorv-example.fr/en

What we need from you?

We’re approaching our 10th birthday and, whilst we still love what we do, we think it’s the right time to update our image.

We’d like you to design us a new PowerPoint template, that will be used for all of our internal and client facing work. You can base your submissions on our existing logo and colour scheme (see files attached) or you can submit your own fresh ideas – after all, we’re not afraid of change!

Finally, whilst we’re looking for you to be creative, there are some simple guidelines that we need you to keep in mind:

1. The Template needs to include both a front cover and a “content” page

2. The front cover needs to:
- Include our logo
- Reflect “who we are” and the type of work that we do

3. The content page needs to:
- Have a predominantly white background
- Be practical to use, making an effective use of the 4:3 standard PPT size
- Include an area across the top of the page for the slide title
- Include areas along the bottom of the page for the page number and date

4. If you decide to propose a new colour scheme, it should be balanced and the “accents” usable

5. The PowerPoint Template needs to be “printer friendly”

6. The fonts you use should be standard

What we don’t want?

To give you as much help as possible, here are some things that we really don’t want:

- Submissions that are dull grey or navy blue, suggesting we’re nothing but boring corporate suits
- Submissions that are Lulette pink or too “soft and cuddly”
- Submissions that use lots of stock images of “happy, smiling, consultants”
- Submissions that will be the height of fashion today, but completely out of date next year

```html
<!DOCTYPE html>
<html lang="en">
<head>
<meta charset="utf-8">
<title>Quorv – PowerPoint Template Proposals</title>
<link rel="stylesheet" href="https://fonts.googleapis.com/css2?family=Didact+Gothic&family=Oswald:wght@300&display=swap">
<style>
  :root {
    --plum: #5e0036;
    --plum-light: #a0507c;
    --plum-pale: #d9b3c7;
    --teal: #2aa39a;
    --glow: #7ff0f5;
    --paper: #ffffff;
    --ink: #3a3a3a;
  }
  * { box-sizing: border-box; margin: 0; padding: 0; }
  html, body { width: 1200px; height: 800px; overflow: hidden; background: var(--paper); }
  .board { position: relative; width: 1200px; height: 800px; font-family: "Didact Gothic", sans-serif; }

  .slide {
    position: absolute;
    background: var(--paper);
    box-shadow: 2px 4px 9px rgba(0,0,0,0.35);
    overflow: hidden;
  }
  .cover-one { left: 33px; top: 33px; width: 500px; height: 397px; }
  .cover-two { left: 667px; top: 33px; width: 504px; height: 398px; }
  .content-page { left: 433px; top: 493px; width: 374px; height: 284px; }

  .brand-lockup { position: absolute; display: flex; flex-direction: column; align-items: flex-end; }
  .wordmark { color: var(--plum); font-family: "Didact Gothic", sans-serif; font-weight: 400; line-height: 1; }
  .tagline { color: var(--teal); font-family: "Didact Gothic", sans-serif; line-height: 1; }

  .cover-one .brand-lockup { left: 0; right: 0; top: 150px; align-items: center; }
  .cover-one .wordmark { font-size: 78px; }
  .cover-one .tagline { font-size: 20px; margin-top: 4px; margin-left: 110px; }

  .cover-two .brand-lockup { left: 96px; top: 130px; }
  .cover-two .wordmark { font-size: 90px; }
  .cover-two .tagline { font-size: 21px; margin-top: 6px; }

  .figure-placeholder {
    position: absolute; left: 350px; top: 94px; width: 128px; height: 280px;
    background: linear-gradient(180deg, #6e0a44, var(--plum));
    border-radius: 40px 40px 6px 6px;
  }
  .floor-band { position: absolute; left: 0; bottom: 0; width: 100%; height: 25px; background: var(--plum); }

  .option-label {
    position: absolute; z-index: 0; width: 320px; text-align: center;
    font-family: "Oswald", sans-serif; font-weight: 300; font-size: 24px;
    letter-spacing: 1px; color: #111; top: 443px;
  }
  .option-label::before {
    content: ""; position: absolute; left: 0; right: 0; top: 20px; height: 16px; z-index: -1;
    background: radial-gradient(ellipse at center, var(--glow) 0%, rgba(127,240,245,0.5) 45%, rgba(127,240,245,0) 72%);
  }
  .label-one { left: 123px; }
  .label-two { left: 767px; }

  .title-bar { position: absolute; left: 0; top: 5px; width: 100%; height: 40px; }
  .slide-title {
    position: absolute; left: 14px; top: 10px; color: var(--paper);
    font-size: 17px; font-weight: 400; line-height: 1;
  }
  .content-page .brand-lockup { right: 18px; top: 8px; }
  .content-page .wordmark { font-size: 20px; }
  .content-page .tagline { font-size: 6px; margin-top: 1px; }

  .body-copy {
    position: absolute; left: 40px; top: 46px; width: 302px;
    font-size: 9px; line-height: 1.2; color: var(--ink);
  }
  .body-copy p { margin-bottom: 11px; }
  .body-copy p.lead-in { margin-top: 20px; margin-bottom: 12px; }
  .body-copy ul { list-style: none; margin-left: 10px; }
  .body-copy li { text-indent: -5px; padding-left: 5px; }

  .page-number {
    position: absolute; right: 8px; bottom: 7px; width: 16px; height: 16px;
    background: var(--plum); color: var(--paper); font-size: 9px;
    display: flex; align-items: center; justify-content: center;
  }
</style>
</head>
<body>
<main class="board">

  <section class="slide cover-one" aria-label="Cover option 1">
    <div class="brand-lockup">
      <span class="wordmark">Quorv</span>
      <span class="tagline">boosting change</span>
    </div>
  </section>
  <div class="option-label label-one">OPTION 1</div>

  <section class="slide cover-two" aria-label="Cover option 2">
    <div class="brand-lockup">
      <span class="wordmark">Quorv</span>
      <span class="tagline">boosting change</span>
    </div>
    <div class="figure-placeholder" role="img" aria-label="Plum silhouette of a standing woman, hands on hips"></div>
    <div class="floor-band"></div>
  </section>
  <div class="option-label label-two">OPTION 2</div>

  <section class="slide content-page" aria-label="Content page">
    <svg class="title-bar" viewBox="0 0 374 40" preserveAspectRatio="none">
      <polygon points="250,0 330,10 225,30" fill="var(--plum-pale)" opacity="0.6"/>
      <polygon points="0,0 250,0 232,24 0,24" fill="var(--plum)"/>
      <polygon points="0,24 232,24 222,29 0,29" fill="var(--plum-light)"/>
    </svg>
    <h1 class="slide-title">Who are we?</h1>
    <div class="brand-lockup">
      <span class="wordmark">Quorv</span>
      <span class="tagline">boosting change</span>
    </div>

    <div class="body-copy">
      <p>Formed in 2005, Quorv is a consulting company specialising in the human aspect of change and transformation.</p>
      <p>From our offices in the heart of Paris, our team of 30 consultants work with leading organisations in the Aerospace, Finance, Transportation and Public sectors to deliver lasting change.</p>
      <p class="lead-in">Our customers trust us with some of their most strategic and sensitive projects. They trust us with these projects because:</p>
      <ul>
        <li>- We listen to them, ensuring we understand the real needs of their business</li>
        <li>- We involve them, co-developing and tailoring our solutions to the specific challenges they face</li>
        <li>- We’re professional, without taking ourselves too seriously</li>
        <li>- We’re imaginative, whilst always remaining pragmatic</li>
        <li>- We get results!</li>
      </ul>
    </div>

    <div class="page-number">1</div>
  </section>

</main>
</body>
</html>
```